Business Card Design Project

We need a business card design for an existing company in Dallas/Fort Worth that is expanding services and re-branding. We are changing the name from Bristow Commercial Cleaning to Kelmont Facility Services. We are expanding from only commercial cleaning to include complete commercial landscape and facility maintenance services, too.

As stated, we offer a package of services that includes landscape, janitorial and facility services, which is largely unique in the industry.

We would like a design that communicates trust/partnership with a professional, corporate image, but not necessarily using the standard white business card. We would like a design that perhaps uses darker blues or perhaps a gray background, but we are open to other ideas. We might also be interested in a double-sided design - maybe with our logo on the back, printed on a gray background?

We will probably stick with the attached logo, but if you've got another inspired idea....

Target Market(s)

Property managers, commercial real estate professionals, corporate executives

Industry/Entity Type

Landscape

Requirements
Should not have
• Not interested in old style fonts.

```html
<!DOCTYPE html>
<html lang="en">
<head>
<meta charset="utf-8">
<title>Kelmont Facility Services – Business Card</title>
<link rel="stylesheet" href="https://fonts.googleapis.com/css2?family=Catamaran:wght@400;600;700&display=swap">
<style>
  :root {
    --navy: #2e2a6b;
    --ink: #2b2b2d;
    --grey-band: #4a4a4c;
    --card-white: #ffffff;
    --card-mist: #e9e9ec;
    --back-grey: #3b3b3e;
    --back-grey-dark: #2c2c2f;
    --stage: #eeeef0;
    --muted: #555559;
  }
  * { box-sizing: border-box; margin: 0; padding: 0; }
  html, body {
    width: 1200px; height: 900px; overflow: hidden;
    background: var(--stage);
    font-family: "Catamaran", Arial, sans-serif;
  }
  .canvas {
    width: 1200px; height: 900px;
    display: flex; flex-direction: column; align-items: center; justify-content: center;
    gap: 36px;
  }
  .card {
    position: relative;
    width: 680px; height: 389px;
    overflow: hidden;
    box-shadow: 0 6px 18px rgba(0,0,0,0.18);
  }

  /* Front */
  .card-front {
    background: linear-gradient(200deg, var(--card-mist) 0%, var(--card-white) 45%);
    color: var(--ink);
  }
  .brand {
    position: absolute; left: 34px; top: 48px;
    display: flex; align-items: flex-end; gap: 14px;
  }
  .brand-square {
    width: 62px; height: 56px;
    border: 5px solid var(--navy);
    flex: none;
  }
  .brand-text { color: var(--ink); font-weight: 600; text-transform: uppercase; line-height: 0.95; }
  .brand-name-main { font-size: 38px; letter-spacing: 3px; }
  .brand-name-sub { font-size: 22px; letter-spacing: 1.5px; }
  .brand-tagline {
    margin-top: 3px;
    font-size: 10.5px; font-weight: 600; color: var(--ink);
    text-transform: none; letter-spacing: 0.2px; line-height: 1.2;
  }
  .person {
    position: absolute; right: 48px; top: 150px;
    text-align: right;
  }
  .person-name { font-size: 24px; font-weight: 700; line-height: 1.1; }
  .person-role { font-size: 16px; color: var(--navy); line-height: 1.3; }
  .person-cell { font-size: 15px; color: var(--ink); line-height: 1.3; }

  .contact {
    position: absolute; left: 34px; top: 228px;
    font-size: 15px; line-height: 1.35; color: var(--muted);
  }
  .contact-address { font-weight: 700; color: var(--ink); }
  .contact-line { display: flex; align-items: center; gap: 6px; }
  .contact-line svg { width: 13px; height: 13px; fill: var(--navy); flex: none; }

  .bands { position: absolute; left: 0; bottom: 0; width: 680px; height: 110px; }
  .front-web {
    position: absolute; right: 22px; bottom: 48px;
    font-size: 15px; color: #fff;
  }
  .front-web strong { font-weight: 700; }

  /* Back */
  .card-back {
    background: radial-gradient(ellipse at center, var(--back-grey) 0%, var(--back-grey-dark) 100%);
    color: #fff;
  }
  .back-brand {
    position: absolute; inset: 0;
    display: flex; align-items: center; justify-content: center; gap: 16px;
  }
  .back-brand .brand-square { border-color: #fff; }
  .back-brand .brand-text { color: #fff; font-size: 28px; letter-spacing: 2px; }
  .back-web {
    position: absolute; right: 30px; bottom: 26px;
    font-size: 14px; color: #e6e6e8;
  }
  .back-web strong { font-weight: 700; }
</style>
</head>
<body>
<main class="canvas">

  <section class="card card-front" aria-label="Business card front">
    <div class="brand">
      <div class="brand-square"></div>
      <div class="brand-text">
        <div class="brand-name-main">Kelmont</div>
        <div class="brand-name-sub">Facility Services</div>
        <div class="brand-tagline">Complete Care For Grounds, Cleaning and Building Upkeep</div>
      </div>
    </div>

    <div class="person">
      <div class="person-name">Dale Harmon</div>
      <div class="person-role">General Manager</div>
      <div class="person-cell">Cell: 972-555-0142</div>
    </div>

    <div class="contact">
      <div class="contact-address">2290 Meadow Ridge Road,<br>Cedar Hollow, TX 75099</div>
      <div class="contact-line">
        <svg viewBox="0 0 16 16" aria-hidden="true"><path d="M3 2h3l1.5 3.5-2 1.2a8 8 0 0 0 3.8 3.8l1.2-2L14 10v3a1 1 0 0 1-1 1A11 11 0 0 1 2 3a1 1 0 0 1 1-1z"/></svg>
        817-555-0126
        <svg viewBox="0 0 16 16" aria-hidden="true"><path d="M2 4h9v9H2zM11 6h3v5h-3zM4 6h5v2H4z"/></svg>
        817-555-0187
      </div>
      <div class="contact-line">
        <svg viewBox="0 0 16 16" aria-hidden="true"><path d="M1 3h14v10H1zM2 4l6 5 6-5v1l-6 5-6-5z" fill-rule="evenodd"/></svg>
        dale@kelmontfacility.com
      </div>
    </div>

    <svg class="bands" viewBox="0 0 680 110" aria-hidden="true">
      <polygon points="0,90 380,90 394,72 680,72 680,110 0,110" fill="var(--navy)"/>
      <polygon points="0,76 372,76 380,66 0,66" fill="var(--grey-band)"/>
      <polygon points="408,40 680,40 680,72 394,72 394,56" fill="var(--navy)"/>
      <rect x="0" y="81" width="376" height="9" fill="#ffffff"/>
    </svg>
    <div class="front-web">www.<strong>kelmontfacility</strong>.com</div>
  </section>

  <section class="card card-back" aria-label="Business card back">
    <div class="back-brand">
      <div class="brand-square"></div>
      <div class="brand-text">Kelmont Facility Services</div>
    </div>
    <div class="back-web">www.<strong>kelmontfacility</strong>.com</div>
  </section>

</main>
</body>
</html>
```